redesign my woocommerce store to a minimalist and modern feel

Hi,i have a store that i quickly put together without much thought for design, here it is torvan( )dek( )ro(.) com i just knew i wanted something simple and minimalistic, our different type of logo is attached, having said that i want a complete redesign the homepage, product page, cart page, and the checkout/payment page, i want something modern and simple, i quite like how our products are displayed currently with the pictures in the homepage but that's about it, everything else is up to you.so just to recap. here is my most important conditions: the design should be minimalist, the design should support Arabic and English

Target Market(s)

Gamers

Industry/Entity Type

Games

Number of Pages Required

4 page

Font styles to use
Sans Serif

Colors

Designer to choose colors to be used in the design.

Requirements
Must have
• Simple and minimalist
• has to support 2 languages, so a drop down or a language switcher should be included in the design
Should not have
• crowded design

```html
<!DOCTYPE html>
<html lang="en">
<head>
<meta charset="utf-8">
<title>Torvandekro – Home</title>
<link href="https://fonts.googleapis.com/css2?family=Open+Sans:wght@400;600;700&family=Play:wght@400;700&display=swap" rel="stylesheet">
<style>
:root{
  --brand:#f04e23;
  --brand-red:#e8202e;
  --ink:#1d1d1d;
  --text:#555;
  --muted:#888;
  --page:#f3f3f3;
  --card:#fff;
  --line:#d7d7d7;
  --footer:#141414;
  --footer-text:#e6e6e6;
}
*{box-sizing:border-box;margin:0;padding:0}
html,body{width:1200px;height:2557px;overflow:hidden}
body{position:relative;background:var(--page);font-family:"Open Sans",sans-serif;color:var(--text)}
.abs{position:absolute}

/* top bar */
.topbar{left:0;top:0;width:1200px;height:38px;background:var(--brand);color:#fff;font-size:13px}
.topbar .item{position:absolute;top:0;height:38px;line-height:38px;display:flex;align-items:center;gap:6px}
.topbar .sep{position:absolute;top:0;width:1px;height:38px;background:rgba(255,255,255,.35)}
.topbar .search{left:628px;width:172px;height:38px;background:rgba(255,255,255,.12);padding-left:14px;line-height:38px}

/* header */
.logo{left:0;width:1200px;top:74px;text-align:center;font-family:"Play",sans-serif;font-weight:700;font-size:34px;color:var(--brand)}
.nav{left:133px;top:161px;width:939px;border-top:1px solid var(--line);display:flex;justify-content:space-between;align-items:center;padding-top:10px;font-size:16px;color:var(--ink)}
.nav a{color:inherit;text-decoration:none;padding:9px 20px;line-height:20px}
.nav a.active{background:var(--brand-red);color:#fff;padding:9px 26px}

/* hero */
.hero{left:133px;top:227px;width:939px;height:465px;background:#fff;box-shadow:0 2px 8px rgba(0,0,0,.18);overflow:hidden}
.hero-art{position:absolute;left:0;top:0;width:939px;height:465px;background:linear-gradient(100deg,#8fc3cf 0%,#ffffff 35%,#f7d873 62%,#c8468f 100%)}
.hero-badge{position:absolute;left:60px;top:90px;width:284px;height:284px;border-radius:50%;background:#fff;box-shadow:0 4px 14px rgba(0,0,0,.2);overflow:hidden}
.hero-badge .top{height:160px;background:var(--brand-red);color:#fff;font-family:"Play",sans-serif;font-weight:700;font-size:34px;text-align:center;padding-top:40px;line-height:40px}
.hero-badge .name{text-align:center;padding-top:44px;font-size:20px;color:var(--ink)}
.hero-dots{position:absolute;left:58px;top:417px;display:flex;gap:4px}
.hero-dots span{width:18px;height:18px;border-radius:50%;background:#555}
.hero-bar{position:absolute;left:445px;top:436px;width:432px;height:7px;border-radius:4px;background:#bbb}

/* section titles */
.section-title{left:0;width:1200px;text-align:center;font-family:"Play",sans-serif;font-weight:700;font-size:30px;color:var(--ink)}
.carousel-arrow{width:26px;height:26px;border-radius:50%;background:#fff;border:1px solid var(--line)}

/* collection */
.product{width:225px;height:239px;background:var(--card);border:1px solid #dcdcdc;box-shadow:0 1px 4px rgba(0,0,0,.1);text-align:center}
.product .thumb{height:123px;background:linear-gradient(#f6f6f6,#e2e2e2);display:flex;align-items:center;justify-content:center;font-family:"Open Sans",sans-serif;font-weight:700;font-size:30px;color:#7a4bd0}
.product h3{font-weight:400;font-size:15px;color:var(--ink);margin-top:14px}
.product .offer{font-size:13px;color:var(--ink);margin-top:4px}
.product .offer b{color:var(--brand-red);font-weight:400}
.product .buy{display:inline-block;margin-top:10px;width:94px;height:26px;line-height:24px;border:1px solid var(--brand-red);color:var(--brand-red);font-size:12px;box-shadow:0 2px 0 #f2b4b8}

/* about */
.about{left:131px;top:1190px;width:942px;height:322px;background:#fff;border:1px solid #dcdcdc}
.about-media{position:absolute;left:0;top:0;width:420px;height:320px;background:linear-gradient(#8f97a3,#5f6772 70%,#20262c)}
.play{position:absolute;left:180px;top:130px;width:60px;height:60px;border-radius:50%;background:rgba(40,40,40,.85)}
.about-copy{position:absolute;left:468px;top:50px;width:420px}
.about-copy h2{font-family:"Play",sans-serif;font-weight:700;font-size:30px;color:var(--ink)}
.about-copy p{font-size:12.5px;line-height:22px;margin-top:18px;text-align:justify}
.btn{display:inline-block;background:var(--brand-red);color:#fff;font-size:13px;padding:6px 16px;margin-top:22px}

/* testimonials */
.quote{width:396px;height:198px;background:#fff;box-shadow:0 2px 8px rgba(0,0,0,.15)}
.avatar{position:absolute;left:-32px;top:44px;width:106px;height:106px;border-radius:50%;background:radial-gradient(circle at 50% 40%,#c49a7a,#6b5a4b);border:3px solid #fff;box-shadow:0 1px 4px rgba(0,0,0,.3)}
.quote h4{position:absolute;left:96px;top:46px;font-weight:400;font-size:15px;color:var(--ink)}
.quote p{position:absolute;left:96px;top:72px;width:270px;font-size:12.5px;line-height:21px;color:var(--muted)}
.quote .who{position:absolute;right:40px;top:144px;font-size:15px;color:var(--brand-red)}
.quote .mark{position:absolute;right:30px;top:6px;font-family:"Play",sans-serif;font-weight:700;font-size:72px;color:var(--brand);line-height:72px}

/* footer */
.footer{left:0;top:2089px;width:1200px;height:468px;background:var(--footer);color:var(--footer-text)}
.payments{left:131px;top:2003px;width:946px;height:123px;background:#fff;display:flex;justify-content:space-around;align-items:center;box-shadow:0 1px 4px rgba(0,0,0,.15)}
.payments span{font-weight:700;font-size:24px;color:#1f3a8a}
.mailing{left:192px;top:2189px;font-family:"Play",sans-serif;font-size:28px;color:#fff}
.subscribe{left:483px;top:2187px;width:406px;height:38px;border-radius:19px;background:#fff;overflow:hidden}
.subscribe .field{position:absolute;left:16px;top:0;line-height:38px;font-size:12px;color:#444}
.subscribe .go{position:absolute;right:0;top:0;width:96px;height:38px;background:var(--brand-red);color:#fff;font-weight:700;font-size:13px;line-height:38px;text-align:center}
.rule{left:133px;width:944px;height:1px;background:#3a3a3a}
.col h5{font-weight:400;font-size:13px;color:#fff;margin-bottom:12px}
.col li{list-style:none;font-size:11px;line-height:22px}
.col li::before{content:"» "}
.col p{font-size:11px;line-height:22px}
.social{display:flex;gap:12px;margin-top:6px}
.social span{width:22px;height:22px;border-radius:4px;background:#e6e6e6}
.copyright{left:0;width:1200px;top:2503px;text-align:center;font-size:11.5px;color:#fff}
</style>
</head>
<body>

<header>
  <div class="abs topbar">
    <div class="item" style="left:133px">
      <svg width="12" height="12" viewBox="0 0 24 24"><path fill="#fff" d="M6.6 10.8a15 15 0 0 0 6.6 6.6l2.2-2.2c.3-.3.7-.4 1-.2 1.1.4 2.3.6 3.6.6.6 0 1 .4 1 1V20c0 .6-.4 1-1 1A17 17 0 0 1 3 4c0-.6.4-1 1-1h3.5c.6 0 1 .4 1 1 0 1.3.2 2.5.6 3.6.1.3 0 .7-.2 1z"/></svg>
      555-010-2040
    </div>
    <div class="sep" style="left:246px"></div>
    <div class="item" style="left:258px">
      <svg width="12" height="10" viewBox="0 0 24 18"><path fill="#fff" d="M0 0h24v2L12 10 0 2zM0 4.5l12 8 12-8V18H0z"/></svg>
      info@torvandekro.com
    </div>
    <div class="item search">Search</div>
    <svg class="abs" style="left:773px;top:13px" width="13" height="13" viewBox="0 0 24 24"><circle cx="10" cy="10" r="7" fill="none" stroke="#fff" stroke-width="3"/><path d="M15 15l7 7" stroke="#fff" stroke-width="3"/></svg>
    <div class="sep" style="left:800px"></div>
    <div class="item" style="left:820px">My account</div>
    <div class="sep" style="left:905px"></div>
    <div class="item" style="left:918px">Eng ▾</div>
    <div class="sep" style="left:966px"></div>
    <svg class="abs" style="left:985px;top:12px" width="13" height="13" viewBox="0 0 24 24"><circle cx="12" cy="7" r="5" fill="#fff"/><path d="M2 23c0-6 4-9 10-9s10 3 10 9z" fill="#fff"/></svg>
    <div class="sep" style="left:1012px"></div>
    <div class="item" style="left:1034px">
      <svg width="14" height="12" viewBox="0 0 24 20"><path fill="#fff" d="M0 0h4l1 3h19l-3 9H7l-1 3h15v2H3l3-6L3 2H0z"/><circle cx="8" cy="19" r="1.6" fill="#fff"/><circle cx="19" cy="19" r="1.6" fill="#fff"/></svg>
      : 0
    </div>
  </div>

  <div class="abs logo">Torvandekro</div>

  <nav class="abs nav">
    <a class="active">Home</a>
    <a>About us</a>
    <a>Collection</a>
    <a>Products</a>
    <a>Online store</a>
    <a>Blog</a>
    <a>Contact us</a>
  </nav>
</header>

<main>
  <section class="abs hero">
    <div class="hero-art" role="img" aria-label="Illustration of a gamer with a VR headset in an armchair surrounded by flying gold coins and colourful swooshes"></div>
    <div class="hero-badge">
      <div class="top">Suits<br>Your Mood</div>
      <div class="name">Torvandekro</div>
    </div>
    <div class="hero-dots"><span></span><span></span></div>
    <div class="hero-bar"></div>
  </section>

  <h2 class="abs section-title" style="top:798px">New Collection</h2>
  <div class="abs carousel-arrow" style="left:124px;top:804px"></div>
  <div class="abs carousel-arrow" style="left:1054px;top:804px"></div>

  <article class="abs product" style="left:131px;top:883px">
    <div class="thumb" style="color:#2f8fe0">lumo</div>
    <h3>Lumo</h3><p class="offer">Buy 2 coin for <b>$5.00</b></p><span class="buy">Buy Now</span>
  </article>
  <article class="abs product" style="left:368px;top:883px">
    <div class="thumb" style="color:#c33bd0">vessa</div>
    <h3>Vessa</h3><p class="offer">Buy 2 coin for <b>$5.00</b></p><span class="buy">Buy Now</span>
  </article>
  <article class="abs product" style="left:607px;top:883px">
    <div class="thumb" style="color:#8a4b1c">darvo</div>
    <h3>Darvo</h3><p class="offer">Buy 2 coin for <b>$5.00</b></p><span class="buy">Buy Now</span>
  </article>
  <article class="abs product" style="left:847px;top:883px">
    <div class="thumb" style="color:#e0306e">kipli</div>
    <h3>Kipli</h3><p class="offer">Buy 2 coin for <b>$5.00</b></p><span class="buy">Buy Now</span>
  </article>

  <section class="abs about">
    <div class="about-media" role="img" aria-label="Video still of a cartoon gamer sitting on a sofa holding a controller, with speakers on each side"></div>
    <div class="play"><svg width="60" height="60" viewBox="0 0 60 60"><path d="M24 18l18 12-18 12z" fill="#fff"/></svg></div>
    <div class="about-copy">
      <h2>About us</h2>
      <p>It is a long established fact that a reader will be distracted by the readable content of a page when looking at its layout. The point of using Lorem Ipsum is that it has a more-or-less normal distribution of letters, as opposed to using 'Content here, content here', making it look like readable English. Many desktop publishing packages</p>
      <span class="btn">Read More</span>
    </div>
  </section>

  <h2 class="abs section-title" style="top:1613px">Testimonials</h2>

  <article class="abs quote" style="left:184px;top:1696px">
    <div class="avatar" role="img" aria-label="Customer portrait photo"></div>
    <span class="mark">“</span>
    <h4>Neque porro quisquam</h4>
    <p>The point of using Lorem Ipsum is that it has a more-or-less normal distribution of letters, as opposed to using 'Content</p>
    <span class="who">-&nbsp;&nbsp;&nbsp;Helen</span>
  </article>
  <article class="abs quote" style="left:655px;top:1696px">
    <div class="avatar" role="img" aria-label="Customer portrait photo"></div>
    <span class="mark">“</span>
    <h4>Dolorem ipsum quia dolor</h4>
    <p>The point of using Lorem Ipsum is that it has a more-or-less normal distribution of letters, as opposed to using 'Content</p>
    <span class="who">- Amet</span>
  </article>
</main>

<footer>
  <div class="abs footer"></div>
  <div class="abs payments">
    <span>Velnorix</span><span style="color:#e0452a">Cardora</span><span style="color:#2d8a4a">Nuvex</span><span style="color:#e05a1e">Settlo</span>
  </div>

  <div class="abs mailing">Join our mailing list</div>
  <div class="abs subscribe"><span class="field">Email@example.com</span><span class="go">SUBSCRIBE</span></div>

  <div class="abs rule" style="top:2273px"></div>

  <div class="abs col" style="left:140px;top:2313px;color:var(--footer-text)">
    <h5>INFORMATION</h5>
    <ul><li>Privacy Policy</li><li>Your Account</li><li>Advanced Search</li><li>Contact Us</li></ul>
  </div>
  <div class="abs col" style="left:360px;top:2313px;color:var(--footer-text)">
    <h5>CUSTOMER SERVICE</h5>
    <ul><li>Safe Shopping Guarantee</li><li>Shipping Rates</li><li>Returns</li><li>Return Policy</li></ul>
  </div>
  <div class="abs col" style="left:625px;top:2313px;color:var(--footer-text)">
    <h5>CONTACT US</h5>
    <p>Address : Nordhal Ltd Kestrel Lane 14<br>40210 Marrow<br>Phone : +00 (0) 155/0142288<br>Email : info@torvandekro.com</p>
  </div>
  <div class="abs col" style="left:915px;top:2309px;color:var(--footer-text)">
    <h5>FOLLOW US OUT THERE</h5>
    <div class="social" aria-label="Social links"><span></span><span></span><span></span><span></span></div>
  </div>

  <div class="abs rule" style="top:2460px"></div>
  <div class="abs copyright">Copyright © 2018. All Rights Reserved</div>
</footer>

</body>
</html>
```